" Trata-se de uma loja de Bolsas e acessórios femininos como: semi jóias, lenços, cintos... porém, o carro chefe serao as Bolsas, que seguirao um padrao de alta qualidade e bom gosto. Assim como o local, onde contamos com pouco mais de 40m² incluindo um mezanino, o espaço como um todo é bonito e bem decorado para receber mulheres modernas que gostam de novidades, de cor, de estilo... queremos que a logomarca traga junto essa ideia. É uma empresa alegre no seu ambiente, com estilo romântico. "

```html
<!DOCTYPE html>
<html lang="pt-BR">
<head>
<meta charset="utf-8">
<title>Lojas Mimos – Cartão de visita</title>
<link rel="stylesheet" href="https://fonts.googleapis.com/css2?family=Crimson+Pro:ital,wght@0,400;0,600;1,400&display=swap">
<style>
  :root {
    --page-bg: #ffffff;
    --card-dark-center: #525252;
    --card-dark-edge: #2f2f2f;
    --card-light: #e8e8e8;
    --ink-dark: #3c3c3c;
    --ink-muted: #9a9a9a;
    --rose: #f28b86;
    --teal: #6fb5bf;
    --silhouette: #4a4a4a;
    --band-ink: #5a2f2c;
  }
  * { box-sizing: border-box; margin: 0; padding: 0; }
  html, body {
    width: 1200px; height: 1200px; overflow: hidden;
    background: var(--page-bg);
    font-family: "Crimson Pro", Georgia, serif;
  }
  .canvas { position: relative; width: 1200px; height: 1200px; }

  .card {
    position: absolute; left: 223px; width: 761px;
    border-radius: 48px; overflow: hidden;
  }

  /* Front */
  .card-front {
    top: 132px; height: 432px;
    background: radial-gradient(ellipse at 50% 40%, var(--card-dark-center), var(--card-dark-edge) 75%);
  }
  .brand {
    position: absolute; left: 0; right: 0; top: 270px;
    display: flex; align-items: center; justify-content: center; gap: 24px;
    transform: translateY(-100%);
  }
  .brand-dot { width: 46px; height: 46px; border-radius: 50%; background: var(--rose); }
  .brand-name {
    font-size: 96px; font-weight: 400; color: var(--rose); line-height: 1;
  }
  .web {
    position: absolute; left: 0; right: 0; top: 364px;
    text-align: center; font-size: 27px; font-weight: 600; color: var(--ink-muted);
    letter-spacing: 0.5px;
  }

  /* Back */
  .card-back {
    top: 612px; height: 420px;
    background: var(--card-light);
  }
  .illustration {
    position: absolute; left: 29px; top: 17px; width: 384px; height: 348px;
    background: linear-gradient(180deg, #555555, var(--silhouette));
    border-radius: 40% 40% 12px 12px / 30% 30% 12px 12px;
  }
  .person {
    position: absolute; left: 427px; top: 100px; width: 260px; text-align: center;
  }
  .person-name { font-size: 44px; font-weight: 600; color: var(--ink-dark); line-height: 1; }
  .person-role { font-size: 24px; font-style: italic; color: var(--teal); margin-top: 2px; }
  .contact {
    position: absolute; left: 407px; width: 300px; text-align: center;
    font-size: 27px; color: #1f1f1f; white-space: nowrap; line-height: 1.2;
  }
  .contact-phone { top: 224px; }
  .contact-email { top: 276px; }
  .address-band {
    position: absolute; left: 0; right: 0; bottom: 0; height: 56px;
    background: var(--rose);
    display: flex; align-items: center; justify-content: center;
    font-size: 23px; color: var(--band-ink); word-spacing: 3px;
  }
</style>
</head>
<body>
<main class="canvas">
  <section class="card card-front">
    <div class="brand">
      <span class="brand-dot"></span>
      <span class="brand-name">Lojas Mimos</span>
    </div>
    <p class="web">www.lojasmimos.com</p>
  </section>

  <section class="card card-back">
    <div class="illustration" role="img" aria-label="Ilustração de dois gatos sentados lado a lado em silhueta cinza escura"></div>
    <div class="person">
      <p class="person-name">Mariana</p>
      <p class="person-role">cargo</p>
    </div>
    <p class="contact contact-phone">11-98765432</p>
    <p class="contact contact-email">mariana@lojasmimos.com</p>
    <div class="address-band">Av: Aurora 450&nbsp; Bairro - Jardim Sul&nbsp;&nbsp; São Paulo&nbsp; SP</div>
  </section>
</main>
</body>
</html>
```